Business Card and Stationary
BrookLamp Consutling
Professional
Peter Varsiklo
8276 Wimbrell Lane
Dublin, OH 43092
pvarsiklo@brooklampconsulting.com
brooklampconsulting.com

```html
<!DOCTYPE html>
<html lang="en">
<head>
<meta charset="utf-8">
<title>BrookLamp Consutling – Business Card</title>
<link rel="stylesheet" href="https://fonts.googleapis.com/css2?family=Open+Sans:wght@400;600;700&display=swap">
<style>
  :root {
    --page-bg: #e9e6e1;
    --card-bg: #ffffff;
    --brand-green: #72bf2f;
    --band-dark: #4a4a4c;
    --text-dark: #4b4b4b;
    --text-body: #3d3d3d;
    --rule: #dcdcdc;
  }
  html, body {
    margin: 0;
    width: 1200px;
    height: 778px;
    overflow: hidden;
    background: var(--page-bg);
    font-family: "Open Sans", Arial, sans-serif;
  }
  .card {
    position: absolute;
    left: 60px;
    top: 159px;
    width: 1080px;
    height: 460px;
    background: var(--card-bg);
    border-radius: 26px;
    overflow: hidden;
    box-shadow: 0 4px 14px rgba(0,0,0,0.18);
  }
  .brand {
    position: absolute;
    left: 70px;
    top: 120px;
    width: 320px;
    text-align: center;
    color: var(--text-dark);
    font-weight: 600;
  }
  .brand-square {
    display: block;
    width: 46px;
    height: 46px;
    margin: 0 auto 22px;
    background: var(--text-dark);
  }
  .brand-name {
    display: block;
    font-size: 44px;
    line-height: 1.1;
    letter-spacing: -0.5px;
  }
  .brand-sub {
    display: block;
    font-size: 21px;
    letter-spacing: 7px;
    margin-top: 6px;
  }
  .divider {
    position: absolute;
    left: 452px;
    top: 38px;
    width: 1px;
    height: 300px;
    background: linear-gradient(var(--card-bg), var(--rule) 15%, var(--rule) 85%, var(--card-bg));
  }
  .contact {
    position: absolute;
    left: 515px;
    top: 58px;
    color: var(--text-body);
  }
  .person-name {
    margin: 0;
    font-size: 31px;
    font-weight: 700;
    line-height: 1.15;
    color: var(--brand-green);
  }
  .person-title {
    margin: 0;
    font-size: 28px;
    font-weight: 600;
    line-height: 1.15;
    color: var(--text-dark);
  }
  .address {
    margin: 52px 0 0;
    font-size: 21px;
    line-height: 31px;
    font-style: normal;
  }
  .details {
    margin: 18px 0 0;
    font-size: 21px;
    line-height: 30px;
  }
  .details-row { display: flex; align-items: center; gap: 8px; }
  .details-row svg { width: 16px; height: 16px; flex: none; }
  .footer-band {
    position: absolute;
    left: 0;
    bottom: 0;
    width: 1080px;
    height: 70px;
  }
  .website {
    position: absolute;
    right: 40px;
    bottom: 14px;
    font-size: 23px;
    font-weight: 600;
    color: #ffffff;
  }
</style>
</head>
<body>
  <div class="card">
    <div class="brand">
      <span class="brand-square"></span>
      <span class="brand-name">BrookLamp</span>
      <span class="brand-sub">Consutling</span>
    </div>

    <div class="divider"></div>

    <div class="contact">
      <p class="person-name">Peter Varsiklo</p>
      <p class="person-title">Title</p>
      <address class="address">8276 Wimbrell Lane<br>Dublin, OH 43092</address>
      <div class="details">
        <div class="details-row">
          <svg viewBox="0 0 16 16" aria-hidden="true"><path d="M3 1.5l3 3-1.6 1.8a9 9 0 0 0 5.3 5.3L11.5 10l3 3-2 2C6.5 15 1 9.5 1 3.5z" fill="#72bf2f"/></svg>
          <span>614-555-0182</span>
        </div>
        <div class="details-row">
          <svg viewBox="0 0 16 16" aria-hidden="true"><rect x="1.5" y="3.5" width="13" height="9" fill="none" stroke="#4b4b4b" stroke-width="1.4"/><path d="M1.5 3.5l6.5 5 6.5-5" fill="none" stroke="#4b4b4b" stroke-width="1.4"/></svg>
          <span>pvarsiklo@brooklampconsulting.com</span>
        </div>
      </div>
    </div>

    <svg class="footer-band" viewBox="0 0 1080 70" aria-hidden="true">
      <polygon points="0,8 548,8 538,34 0,34" fill="var(--brand-green)"/>
      <polygon points="538,10 1080,10 1080,70 514,70" fill="var(--band-dark)"/>
    </svg>
    <div class="website">www.brooklampconsulting.com</div>
  </div>
</body>
</html>
```